Innovative modern square business card design for law firm

We require a highly modern innovative styled SQUARE business card (double sided) design & layout for our law firm (PLUS an accompanying letterhead design), which specialises mainly in criminal defence. However included somewhere in the design should display the icons representative of all four different areas of law in which the firm offers services. Each card to display the name of the lawyer, job title, telephone number, switchboard, email, web address, facebook & twitter details + physical address. Attached is the main logo + icons of each of the other departments to be included as well as the firms main overhaul icon (all of which can be used or blended into the overall in some way.(note. high res versions of these icons can be provided if required by the design))

Industry/Entity Type

Law Firm

```html
<!DOCTYPE html>
<html lang="en">
<head>
<meta charset="utf-8">
<title>Harwell Defence – Square Business Card</title>
<link rel="stylesheet" href="https://fonts.googleapis.com/css2?family=Cinzel:wght@600&family=Arimo:wght@400;700&display=swap">
<style>
  :root {
    --surface: #2a2b2d;
    --navy: #062c49;
    --paper: #f2f2f2;
    --ink: #1f2a33;
    --muted: #4a5560;
    --white: #ffffff;
    --dept-red: #d9262b;
    --dept-orange: #e8761f;
    --dept-green: #1d3a1f;
    --dept-blue: #1f3a9a;
  }
  * { box-sizing: border-box; margin: 0; padding: 0; }
  html, body { width: 1200px; height: 1000px; overflow: hidden; }
  body {
    background: var(--surface);
    font-family: "Arimo", Arial, sans-serif;
    display: flex; align-items: center; justify-content: center;
    gap: 40px;
  }
  .card {
    width: 520px; height: 520px; position: relative; flex: none;
    box-shadow: 0 10px 30px rgba(0,0,0,.45);
  }

  /* Front */
  .card-front { background: var(--navy); color: var(--white); }
  .front-brand {
    position: absolute; left: 60px; top: 150px;
    display: flex; align-items: center; gap: 22px;
  }
  .brand-mark { width: 96px; height: 96px; background: var(--white); flex: none; }
  .brand-name {
    font-family: "Cinzel", Georgia, serif; font-weight: 600;
    font-size: 42px; line-height: 1.1; letter-spacing: 2px; color: var(--white);
  }
  .front-phone {
    position: absolute; left: 60px; top: 272px;
    font-size: 15px; letter-spacing: 0.5px; color: var(--white);
  }
  .departments {
    position: absolute; left: 60px; top: 340px; display: flex; gap: 52px;
  }
  .dept { width: 30px; height: 30px; }
  .dept--criminal { background: var(--dept-red); }
  .dept--family { background: var(--dept-orange); }
  .dept--civil { background: var(--dept-green); }
  .dept--property { background: var(--dept-blue); }

  /* Back */
  .card-back { background: var(--paper); color: var(--ink); }
  .back-brand {
    position: absolute; left: 50px; top: 50px; display: flex; align-items: center; gap: 12px;
  }
  .back-brand .brand-mark { width: 46px; height: 46px; background: var(--navy); }
  .back-brand .brand-name { font-size: 22px; letter-spacing: 1px; color: var(--navy); }
  .back-phone { position: absolute; left: 50px; top: 104px; font-size: 10px; color: var(--navy); }
  .social { position: absolute; left: 50px; top: 140px; list-style: none; }
  .social li {
    display: flex; align-items: center; gap: 12px;
    font-size: 19px; letter-spacing: 1px; color: var(--muted); margin-bottom: 6px;
  }
  .social-dot { width: 20px; height: 20px; border: 2px solid var(--navy); border-radius: 50%; }
  .website { position: absolute; left: 50px; top: 218px; font-size: 18px; letter-spacing: 1px; color: var(--muted); }
  .website strong { color: var(--navy); }

  .person { position: absolute; left: 232px; top: 286px; }
  .person-name { font-size: 26px; font-weight: 700; letter-spacing: 2px; color: var(--ink); }
  .person-role { font-size: 16px; letter-spacing: 5px; color: var(--muted); margin-top: 2px; }
  .contact {
    position: absolute; left: 212px; top: 350px;
    border-left: 1px solid var(--navy); padding-left: 20px;
  }
  .contact-row { display: flex; align-items: center; gap: 10px; font-size: 17px; letter-spacing: 1.5px; color: var(--muted); margin-bottom: 4px; }
  .contact-row svg { fill: var(--navy); flex: none; }
  .address-label { font-size: 16px; font-weight: 700; color: var(--navy); margin-top: 8px; }
  .address { font-size: 16px; letter-spacing: 1.5px; color: var(--muted); line-height: 1.25; }
</style>
</head>
<body>

  <section class="card card-front" aria-label="Card front">
    <div class="front-brand">
      <span class="brand-mark"></span>
      <span class="brand-name">Harwell<br>Defence</span>
    </div>
    <p class="front-phone">0800 555 0199 (24hrs)</p>
    <div class="departments" aria-label="Practice areas">
      <span class="dept dept--criminal"></span>
      <span class="dept dept--family"></span>
      <span class="dept dept--civil"></span>
      <span class="dept dept--property"></span>
    </div>
  </section>

  <section class="card card-back" aria-label="Card back">
    <div class="back-brand">
      <span class="brand-mark"></span>
      <span class="brand-name">Harwell Defence</span>
    </div>
    <p class="back-phone">0800 555 0199 (24hrs)</p>
    <ul class="social">
      <li><span class="social-dot"></span>username</li>
      <li><span class="social-dot"></span>username</li>
    </ul>
    <p class="website">www.<strong>website</strong>.com</p>

    <div class="person">
      <p class="person-name">JordanVale</p>
      <p class="person-role">Designer</p>
    </div>
    <div class="contact">
      <p class="contact-row">
        <svg width="14" height="14" viewBox="0 0 24 24" aria-hidden="true"><path d="M6.6 10.8a15.1 15.1 0 0 0 6.6 6.6l2.2-2.2a1 1 0 0 1 1-.25 11.4 11.4 0 0 0 3.6.57 1 1 0 0 1 1 1V20a1 1 0 0 1-1 1A17 17 0 0 1 3 4a1 1 0 0 1 1-1h3.5a1 1 0 0 1 1 1c0 1.25.2 2.45.57 3.57a1 1 0 0 1-.25 1z"/></svg>
        123.456.789
      </p>
      <p class="contact-row">
        <svg width="14" height="12" viewBox="0 0 24 18" aria-hidden="true"><path d="M0 0h24v18H0z"/><path d="M2 2l10 8 10-8" fill="none" stroke="#f2f2f2" stroke-width="2"/></svg>
        Name@website.com
      </p>
      <p class="address-label">Address</p>
      <p class="address">123 AN ST., location,<br>country</p>
    </div>
  </section>

</body>
</html>
```